New Business Card

We need to refresh our business cards. We designed these ourselves and we have no graphic design experience. We would like to find a new business card design that is professional and unique. We are an auto finance company. Feel free to play with the logo, but we would like to keep the eye very present on the card. Our corporate colors are green, grey, and white.
Green - RGB - 168,215,27; HEX - #AADD22
Grey - RGB - 196,196,196; HEX - #C4C4C4
Updates
Need to upload the vector file to finalize the project. The last logo was for a jpeg that didn't stretch well.
Industry/Entity Type
Financial Service
Contact Information for Business Card
Honestly don't know...I need your help!

```html
<!DOCTYPE html>
<html lang="en">
<head>
<meta charset="utf-8">
<title>Brightline Capital – Business Card</title>
<link href="https://fonts.googleapis.com/css2?family=Open+Sans:wght@400;600&display=swap" rel="stylesheet">
<style>
  :root {
    --brand-green: #aadd22;
    --brand-grey: #c4c4c4;
    --card-black: #1d1d1f;
    --ink-white: #f4f4f4;
    --backdrop: #3a3a3c;
  }
  * { margin: 0; padding: 0; box-sizing: border-box; }
  html, body {
    width: 799px; height: 1200px; overflow: hidden;
    background: var(--backdrop);
    font-family: "Open Sans", sans-serif;
  }
  .canvas {
    position: relative; width: 799px; height: 1200px;
    display: flex; flex-direction: column; justify-content: space-around; align-items: center;
    padding: 60px 0;
  }
  .card {
    position: relative; width: 620px; height: 354px;
    background: var(--card-black);
    border-radius: 30px;
    overflow: hidden;
  }
  .brand {
    position: absolute; display: flex; align-items: center; gap: 14px;
    color: var(--brand-green); font-weight: 600; white-space: nowrap;
  }
  .brand-dot { border-radius: 50%; background: var(--brand-green); flex: none; }
  .card-front .brand { left: 50%; top: 50%; transform: translate(-50%, -50%); font-size: 46px; }
  .card-front .brand-dot { width: 38px; height: 38px; }
  .card-back .brand { right: 40px; bottom: 60px; font-size: 30px; gap: 10px; }
  .card-back .brand-dot { width: 24px; height: 24px; }

  .edge-crescent { position: absolute; left: 0; top: 18px; }
  .holder { position: absolute; left: 52px; top: 34px; }
  .holder-name { color: var(--brand-green); font-weight: 600; font-size: 22px; line-height: 1.2; }
  .holder-title { color: var(--ink-white); font-size: 13px; margin-top: 2px; }

  .contact { position: absolute; left: 36px; bottom: 40px; list-style: none; color: var(--ink-white); font-size: 15px; line-height: 1.55; }
  .contact li { display: flex; align-items: center; gap: 12px; }
  .contact svg { width: 14px; height: 14px; flex: none; fill: var(--brand-green); }
  .contact .address { margin-top: 2px; }
</style>
</head>
<body>
<main class="canvas">
  <section class="card card-front" aria-label="Card front">
    <div class="brand"><span class="brand-dot"></span>Brightline Capital</div>
  </section>

  <section class="card card-back" aria-label="Card back">
    <svg class="edge-crescent" width="40" height="90" viewBox="0 0 40 90" aria-hidden="true">
      <path d="M0 0 Q34 4 38 45 Q34 86 0 90 Q18 45 0 0 Z" fill="var(--brand-green)"/>
    </svg>
    <div class="holder">
      <p class="holder-name">Daniel Reyes Ortiz</p>
      <p class="holder-title">Managing Director</p>
    </div>
    <ul class="contact">
      <li><svg viewBox="0 0 16 16" aria-hidden="true"><path d="M3 1h3l1 4-2 1a9 9 0 0 0 5 5l1-2 4 1v3a2 2 0 0 1-2 2A13 13 0 0 1 1 3a2 2 0 0 1 2-2z"/></svg>555.010.2040</li>
      <li><svg viewBox="0 0 16 16" aria-hidden="true"><path d="M1 3h14v10H1z M1 3l7 6 7-6" stroke="var(--card-black)" stroke-width="1.2"/></svg>dreyes@brightlinecapital.com</li>
      <li><svg viewBox="0 0 16 16" aria-hidden="true"><circle cx="8" cy="8" r="7"/><path d="M1 8h14M8 1c-3 4-3 10 0 14M8 1c3 4 3 10 0 14" stroke="var(--card-black)" stroke-width="1" fill="none"/></svg>www.brightlinecapital.com</li>
      <li class="address">87 Harbor Lane, Fairview, ST, US 54321</li>
    </ul>
    <div class="brand"><span class="brand-dot"></span>Brightline Capital</div>
  </section>
</main>
</body>
</html>
```